Oil Field Service company needs professional business cards

Looking to clean up our current company business cards and look a little more professional. Harlow Tubular Services is a US based company that services the oil field. We deal with engineers, managers and oil rigs....................................................................................................................................................................................................................................................................................................................................................................................................

Target Market(s)

Oil and Gas professionals

Industry/Entity Type

Oil And Gas

Contact Information for Business Card

See attached photo as example

Font styles to use
Sans Serif

Colors
ec1f27

Requirements
Must have
• Company Logo, Name, Title, Cell, Office, Fax, Email.
• See attached photo
Nice to have
• External CRT, Internal CRT, Casing Crews, Torque Turn, Laydown Machine
Should not have
• Do not introduce any new pictures and keep it professional looking

```html
<!DOCTYPE html>
<html lang="en">
<head>
<meta charset="utf-8">
<title>Harlow Tubular Services – Business Card</title>
<link rel="stylesheet" href="https://fonts.googleapis.com/css2?family=Roboto:wght@400;500;700;900&display=swap">
<style>
  :root {
    --brand-red: #e3232b;
    --ink-slate: #3d4a55;
    --ink-dark: #333333;
    --card-white: #ffffff;
    --divider: #b9b9b9;
    --backdrop: #d6d6d6;
  }
  * { box-sizing: border-box; margin: 0; padding: 0; }
  html, body {
    width: 1200px;
    height: 1000px;
    overflow: hidden;
    background: var(--backdrop);
    font-family: "Roboto", Arial, sans-serif;
  }
  .business-card {
    position: absolute;
    left: 75px;
    top: 200px;
    width: 1050px;
    height: 600px;
    border-radius: 40px;
    background: var(--card-white);
    overflow: hidden;
    box-shadow: 0 10px 30px rgba(0,0,0,0.18);
  }
  .card-art {
    position: absolute;
    inset: 0;
  }
  .brand-block {
    position: absolute;
    left: 70px;
    top: 180px;
    width: 400px;
    text-align: center;
  }
  .brand-name {
    display: flex;
    align-items: center;
    justify-content: center;
    gap: 14px;
    font-weight: 900;
    font-size: 29px;
    line-height: 1.15;
    color: var(--ink-slate);
    text-transform: uppercase;
  }
  .brand-mark {
    width: 22px;
    height: 22px;
    background: var(--brand-red);
    flex: none;
  }
  .brand-address {
    margin-top: 22px;
    font-size: 21px;
    color: var(--ink-dark);
  }
  .divider {
    position: absolute;
    left: 505px;
    top: 95px;
    width: 2px;
    height: 250px;
    background: linear-gradient(var(--divider), #e5e5e5);
  }
  .contact-block {
    position: absolute;
    left: 545px;
    top: 92px;
  }
  .contact-name {
    font-size: 34px;
    font-weight: 700;
    color: var(--brand-red);
  }
  .contact-title {
    font-size: 22px;
    color: var(--ink-dark);
    margin-top: 2px;
    margin-bottom: 14px;
  }
  .contact-list { list-style: none; }
  .contact-item {
    display: flex;
    align-items: center;
    gap: 18px;
    font-size: 23px;
    color: var(--ink-dark);
    height: 36px;
  }
  .contact-icon {
    width: 22px;
    height: 22px;
    flex: none;
    fill: none;
    stroke: var(--brand-red);
    stroke-width: 2;
  }
  .contact-icon.solid { fill: var(--brand-red); stroke: none; }
  .services-line {
    font-size: 22px;
    fill: var(--ink-dark);
    letter-spacing: 0.3px;
  }
</style>
</head>
<body>
  <div class="business-card">
    <svg class="card-art" width="1050" height="600" viewBox="0 0 1050 600">
      <path class="red-swoosh" fill="var(--brand-red)"
            d="M0,600 L0,560 C280,560 620,470 1050,290 L1050,600 Z"/>
      <path id="services-curve" fill="none" d="M0,526 C280,526 620,436 1050,256"/>
      <text class="services-line">
        <textPath href="#services-curve" startOffset="250">Laydown Machine | Casing Crew | Mud Tools | Torque Turn</textPath>
      </text>
    </svg>

    <div class="brand-block">
      <div class="brand-name"><span class="brand-mark"></span>Harlow Tubular Services</div>
      <p class="brand-address">Redfield, OK 73000</p>
    </div>

    <div class="divider"></div>

    <div class="contact-block">
      <h1 class="contact-name">Cody Marsh</h1>
      <p class="contact-title">Area Manager</p>
      <ul class="contact-list">
        <li class="contact-item">
          <svg class="contact-icon" viewBox="0 0 22 22"><rect x="6" y="2" width="10" height="18" rx="2"/><line x1="10" y1="17" x2="12" y2="17"/></svg>
          (555) 214 0187
        </li>
        <li class="contact-item">
          <svg class="contact-icon solid" viewBox="0 0 22 22"><path d="M5 3 L9 3 L10 8 L7.5 9.5 C9 12.5 10.5 14 13.5 15.5 L15 13 L20 14 L20 18 C20 19 19 20 18 20 C10 19.5 3.5 13 3 5 C3 4 4 3 5 3 Z"/></svg>
          (555) 362 4091
        </li>
        <li class="contact-item">
          <svg class="contact-icon solid" viewBox="0 0 22 22"><rect x="6" y="2" width="10" height="6"/><rect x="2" y="9" width="18" height="8" rx="1"/><rect x="6" y="15" width="10" height="5" fill="#fff" stroke="var(--brand-red)" stroke-width="1.5"/></svg>
          (555) 214 0190
        </li>
        <li class="contact-item">
          <svg class="contact-icon" viewBox="0 0 22 22"><rect x="2" y="5" width="18" height="12"/><polyline points="2,5 11,12 20,5"/></svg>
          yourname@email.com
        </li>
      </ul>
    </div>
  </div>
</body>
</html>
```